Clean invitation for a wedding

Design a wedding invitation.
Those examples in attachment. They are looking for this style, about the same construction. Back with the symbols etc.

Clean sleek design.

marriage name:
Kemp & Rosetta
02.06.23

You can copy the rest of the texts from the examples.

```html
<!DOCTYPE html>
<html lang="da">
<head>
<meta charset="utf-8">
<title>Kemp &amp; Rosetta – Bryllupsinvitation</title>
<link rel="stylesheet" href="https://fonts.googleapis.com/css2?family=Sacramento&family=Jost:wght@400&family=Old+Standard+TT&display=swap">
<style>
  :root {
    --backdrop: #241b18;
    --paper: #e8e1d8;
    --ink: #3a2e2a;
    --rule: #7a6c66;
  }
  * { box-sizing: border-box; margin: 0; padding: 0; }
  html, body {
    width: 1200px; height: 1177px; overflow: hidden;
    background: var(--backdrop);
  }
  .stage { position: relative; width: 1200px; height: 1177px; }
  .card {
    position: absolute; top: 210px;
    width: 540px; height: 756px;
    background: var(--paper);
    color: var(--ink);
    font-family: "Jost", sans-serif;
  }
  .card--program { left: 40px; }
  .card--invitation { left: 620px; text-align: center; }

  /* Program card */
  .program-title {
    position: absolute; top: 60px; left: 0; width: 100%;
    text-align: center;
    font-family: "Sacramento", cursive;
    font-size: 84px; line-height: 1;
  }
  .timeline {
    position: absolute; left: 0; top: 0; width: 540px; height: 756px;
  }
  .timeline-rule {
    position: absolute; left: 199px; top: 225px; width: 1px; height: 470px;
    background: var(--rule);
  }
  .event { position: absolute; left: 0; width: 540px; height: 62px; }
  .event-time {
    position: absolute; right: 370px; top: 28px;
    font-size: 18px; letter-spacing: 0.5px;
  }
  .event-icon {
    position: absolute; left: 169px; top: 0;
    width: 62px; height: 62px; border-radius: 50%;
    border: 1.3px solid var(--ink); background: var(--paper);
    display: flex; align-items: center; justify-content: center;
  }
  .event-icon svg { width: 40px; height: 40px; fill: none; stroke: var(--ink); stroke-width: 1.6; stroke-linecap: round; stroke-linejoin: round; }
  .event-icon .figure-fill { width: 38px; height: 38px; border-radius: 50%; background: #cfc5ba; }
  .event-label {
    position: absolute; left: 262px; top: 2px;
    font-size: 17px; line-height: 1.2; letter-spacing: 0.8px;
  }

  /* Invitation card */
  .couple {
    position: absolute; top: 58px; left: 0; width: 100%;
    font-family: "Sacramento", cursive;
    font-size: 92px; line-height: 100px;
  }
  .couple-amp { display: block; font-size: 72px; margin: 8px 0; }
  .guests {
    position: absolute; top: 364px; left: 0; width: 100%;
    font-size: 17px; letter-spacing: 0.6px;
  }
  .message {
    position: absolute; top: 412px; left: 40px; right: 40px;
    font-size: 17px; line-height: 24px; letter-spacing: 0.6px;
  }
  .date {
    position: absolute; top: 502px; left: 0; width: 100%;
    font-family: "Old Standard TT", serif;
    font-size: 40px; letter-spacing: 1px;
  }
  .venues {
    position: absolute; top: 600px; left: 0; width: 100%; height: 110px;
    display: flex; justify-content: center;
  }
  .venue { width: 220px; padding: 0 18px; }
  .venue--ceremony { text-align: right; border-right: 1px solid var(--rule); }
  .venue--party { text-align: left; }
  .venue-heading {
    font-family: "Old Standard TT", serif;
    font-size: 23px; letter-spacing: 1px; margin-bottom: 22px;
  }
  .venue-place { font-size: 17px; line-height: 22px; letter-spacing: 0.4px; }
</style>
</head>
<body>
<main class="stage">

  <section class="card card--program" aria-label="Program">
    <h2 class="program-title">Program</h2>
    <div class="timeline">
      <div class="timeline-rule"></div>

      <div class="event" style="top:200px">
        <span class="event-time">13:30</span>
        <span class="event-icon">
          <svg viewBox="0 0 40 40"><circle cx="15" cy="24" r="9"/><circle cx="25" cy="24" r="9"/><path d="M17 11l3-4 3 4-3 3z"/></svg>
        </span>
        <span class="event-label">VIELSE</span>
      </div>

      <div class="event" style="top:295px">
        <span class="event-time">15:00</span>
        <span class="event-icon">
          <svg viewBox="0 0 40 40"><path d="M9 12l6 2-1 8a3 3 0 0 1-5-2z"/><path d="M11.5 22l-2 9M7 31h5"/><path d="M31 12l-6 2 1 8a3 3 0 0 0 5-2z"/><path d="M28.5 22l2 9M28 31h5"/><path d="M20 6v3M17 8l1 1M23 8l-1 1"/></svg>
        </span>
        <span class="event-label">FORFRISKNINGER<br>OG HYGGE</span>
      </div>

      <div class="event" style="top:390px">
        <span class="event-time">16:00</span>
        <span class="event-icon">
          <svg viewBox="0 0 40 40"><rect x="8" y="26" width="24" height="7"/><rect x="11" y="19" width="18" height="7"/><rect x="14" y="13" width="12" height="6"/><path d="M20 13V8M6 33h28"/></svg>
        </span>
        <span class="event-label">BRYLLUPSKAGE</span>
      </div>

      <div class="event" style="top:485px">
        <span class="event-time">17:30</span>
        <span class="event-icon">
          <svg viewBox="0 0 40 40"><path d="M8 28a12 12 0 0 1 24 0z"/><path d="M5 28h30M6 31h28"/><circle cx="20" cy="15" r="1.5"/><path d="M15 10c-1-2 1-3 0-5M20 9c-1-2 1-3 0-5M25 10c-1-2 1-3 0-5"/></svg>
        </span>
        <span class="event-label">MIDDAG</span>
      </div>

      <div class="event" style="top:580px">
        <span class="event-time">19:00</span>
        <span class="event-icon">
          <span class="figure-fill" role="img" aria-label="Dansende brudepar"></span>
        </span>
        <span class="event-label">BRUDEVALS</span>
      </div>

      <div class="event" style="top:675px">
        <span class="event-time">23:00</span>
        <span class="event-icon">
          <svg viewBox="0 0 40 40"><path d="M16 28V13l12-3v15"/><circle cx="13" cy="28" r="3"/><circle cx="25" cy="25" r="3"/><path d="M9 12l1 2 2 1-2 1-1 2-1-2-2-1 2-1zM31 29l1 1.5 1.5 1-1.5 1-1 1.5-1-1.5-1.5-1 1.5-1z"/></svg>
        </span>
        <span class="event-label">MUSIC</span>
      </div>
    </div>
  </section>

  <section class="card card--invitation" aria-label="Invitation">
    <h1 class="couple">Kemp<span class="couple-amp">&amp;</span>Rosetta</h1>
    <p class="guests">LISE MARIE &amp; TORBEN</p>
    <p class="message">VI SKAL GIFTES OG DET VIL DERFOR GLÆDE OS<br>MEGET AT SE JER TIL VORES BRYLLUPSFEST</p>
    <p class="date">02. 06. 23</p>
    <div class="venues">
      <div class="venue venue--ceremony">
        <h3 class="venue-heading">VIELSE</h3>
        <p class="venue-place">EGEBAKKE KIRKE<br>AARHUS</p>
      </div>
      <div class="venue venue--party">
        <h3 class="venue-heading">FEST</h3>
        <p class="venue-place">STRANDLY BADEHOTEL<br>SKODSTRUP</p>
      </div>
    </div>
  </section>

</main>
</body>
</html>
```